Flyer Design Project

We need a flyer design for a 1 year old domestic cleaning company based in Wiltshire, England. We provide households with high quality, hard working cleaners. We would like to see designs which use blue (the colour on the logo attatched). The final design should communicate a clean, premier and thorough service in a clear and bold way. We would like the flyer to be A5 with a single sided design. We have attached an A5 word document with the words we would like to be used in the design, what we need is for you to give it some life, colour, artwork and a professional touch. We are perfectionsists which we would like to illustrate to our customer through this flyer.
Updates

payment has been guaranteed!

Sorry..... please no pictures of females on the designs. many thanks

Target Market(s)

females with higher than average income, aged 30-50. Have families and work 9-5.

Industry/Entity Type

It Company

Requirements
Must have
• The flyer must include the logo attatched and the words in the A5 document attatched. With RELIABLE CLEANERS preferably the headline. A5 - single sided.
The Flyer must also include our introductory offer.....
First Clean FREE
Allow us to demonstrate our standards

this should be emphasised.

PLEASE NOTE: can this be added to the list of words on the flyer please:

Ironing service - one day turn around
Nice to have
• some pictures - nothing cheesey. Again, pictures should communicate our modern professional approach.

```html
<!DOCTYPE html>
<html lang="en">
<head>
<meta charset="utf-8">
<title>Reliable Cleaners – Flyer</title>
<link rel="stylesheet" href="https://fonts.googleapis.com/css2?family=Rubik:wght@800&family=Libre+Baskerville:wght@700&family=Carlito&display=swap">
<style>
  :root {
    --slate-top: #364353;
    --slate-mid: #55667a;
    --blue-glow: #4f86c8;
    --sand-glow: #c9a978;
    --floor: #e7ebee;
    --glass-edge: rgba(255, 255, 255, 0.85);
    --glass-fill: rgba(255, 255, 255, 0.10);
    --frame-line: rgba(225, 235, 242, 0.55);
    --emboss-text: #9fb7c0;
    --emboss-dark: #24303b;
    --emboss-light: rgba(255, 255, 255, 0.55);
    --title-metal: #d7dfe6;
    --title-outline: #2a3440;
    --brand-navy: #1b2140;
    --brand-blue: #1f5fae;
  }
  * { margin: 0; padding: 0; box-sizing: border-box; }
  html, body { width: 845px; height: 1200px; overflow: hidden; }
  .flyer {
    position: relative;
    width: 845px;
    height: 1200px;
    overflow: hidden;
    background:
      radial-gradient(ellipse 420px 600px at 0% 62%, rgba(79,134,200,0.95), transparent 70%),
      radial-gradient(ellipse 380px 560px at 100% 70%, rgba(201,169,120,0.9), transparent 70%),
      linear-gradient(180deg, var(--slate-top) 0%, var(--slate-mid) 60%, #7b8a99 82%);
  }
  .floor {
    position: absolute;
    left: 0; right: 0; top: 985px; bottom: 0;
    background: linear-gradient(180deg, rgba(215,225,232,0.75) 0%, var(--floor) 35%, #f4f6f7 100%);
  }
  .glass-panel {
    position: absolute;
    left: 123px; top: 96px;
    width: 613px; height: 1011px;
    border-radius: 78px;
    border: 4px solid var(--glass-edge);
    background: linear-gradient(160deg, rgba(255,255,255,0.18), var(--glass-fill) 45%, rgba(255,255,255,0.06));
    box-shadow: 0 0 18px rgba(255,255,255,0.35), inset 0 0 14px rgba(255,255,255,0.25);
  }
  .glass-sheen {
    position: absolute;
    left: 123px; top: 96px;
    width: 613px; height: 1011px;
  }
  .inner-frame {
    position: absolute;
    left: 211px; top: 162px;
    width: 436px; height: 878px;
    border: 2px solid var(--frame-line);
  }
  .headline {
    position: absolute;
    left: 0; width: 845px; top: 108px;
    text-align: center;
    font-family: "Rubik", sans-serif;
    font-weight: 800;
    font-size: 46px;
    letter-spacing: 4px;
    color: var(--title-metal);
    text-shadow:
      -2px -2px 0 var(--title-outline), 2px -2px 0 var(--title-outline),
      -2px 2px 0 var(--title-outline), 2px 2px 0 var(--title-outline),
      3px 4px 4px rgba(0,0,0,0.45);
  }
  .emboss {
    font-family: "Libre Baskerville", serif;
    font-weight: 700;
    color: var(--emboss-text);
    text-shadow: 1px 1px 1px var(--emboss-dark), -1px -1px 0 var(--emboss-light), 2px 3px 3px rgba(0,0,0,0.35);
    position: absolute;
    left: 215px;
  }
  .offer { top: 236px; font-size: 42px; }
  .offer-sub { top: 330px; font-size: 23px; line-height: 30px; width: 420px; }
  .benefits { top: 414px; list-style: none; font-size: 23px; line-height: 30.5px; }
  .divider {
    position: absolute;
    left: 213px; width: 430px; height: 3px;
    background: linear-gradient(180deg, rgba(255,255,255,0.6), rgba(40,55,70,0.5));
  }
  .divider-top { top: 638px; }
  .divider-bottom { top: 828px; }
  .contact { top: 664px; font-size: 23px; line-height: 33px; }
  .brand {
    position: absolute;
    left: 213px; top: 920px;
    display: flex; align-items: center; gap: 14px;
  }
  .brand-square { width: 50px; height: 50px; background: var(--brand-blue); }
  .brand-name {
    font-family: "Carlito", sans-serif;
    font-size: 45px;
    color: var(--brand-navy);
  }
  .tagline {
    position: absolute;
    left: 0; width: 900px; top: 1006px;
    text-align: center;
    font-family: "Carlito", sans-serif;
    font-size: 24px;
    color: var(--brand-navy);
  }
</style>
</head>
<body>
  <main class="flyer">
    <div class="floor"></div>
    <div class="glass-panel"></div>
    <svg class="glass-sheen" viewBox="0 0 613 1011" aria-hidden="true">
      <polygon points="180,20 530,20 20,700 20,330" fill="rgba(255,255,255,0.07)"/>
      <polygon points="560,40 600,120 200,1000 150,1000" fill="rgba(255,255,255,0.04)"/>
    </svg>
    <div class="inner-frame"></div>

    <h1 class="headline">Reliable Cleaners</h1>

    <p class="emboss offer">First Clean FREE!</p>
    <p class="emboss offer-sub">Allow us to demonstrate our standards...</p>
    <ul class="emboss benefits">
      <li>Personalised service</li>
      <li>Constantly thorough</li>
      <li>Hassel free</li>
      <li>Insured</li>
      <li>Regular weekly cleans</li>
      <li>No contracts</li>
    </ul>

    <div class="divider divider-top"></div>
    <address class="emboss contact" style="font-style:normal">
      Tele:<br>07700900123<br>Email:<br>brightmoorclean@example.co.uk
    </address>
    <div class="divider divider-bottom"></div>

    <div class="brand">
      <span class="brand-square"></span>
      <span class="brand-name">Brightmoor Cleaners</span>
    </div>
    <p class="tagline">Premier Domestic Cleaners</p>
  </main>
</body>
</html>
```